Project Sign for Construction Company

Site contractor needs a 4'x8' sign to place on construction sites for advertising. Our company builds the infrastructure for new housing developments. These sign will be posted on the road side to be viewed by passing cars. I want a clean and bold look and feel that resembles my company logo.

Font styles to use
Other font styles liked:
• Hypatia Sans Pro

Colors

Designer to choose colors to be used in the design.

Requirements
Must have
• 555-382-9146 | Info@MarlowPaving.example
• CUC 8047319
• www.MarlowPaving.example
• Services
• Road Construction
• Site Preparation & Excavation
• Underground Utilities
• Shoreline Restoration
Nice to have
• Now Hiring
• Pipe Layers
• Foremen
• Equipment Operators
Should not have
• Should not have stock picture images used in the design, focus on logo and geometric shapes

```html
<!DOCTYPE html>
<html lang="en">
<head>
<meta charset="utf-8">
<title>Marlow Paving – Site Sign</title>
<link href="https://fonts.googleapis.com/css2?family=Alegreya+Sans:wght@500;700;800;900&display=swap" rel="stylesheet">
<style>
  :root {
    --brand-blue: #0457a6;
    --panel-grey: #6f7073;
    --ink-black: #1b1b1c;
    --paper: #f4f4f5;
    --paper-shade: #e3e4e6;
    --white: #ffffff;
    --stage: #e8e8e8;
  }
  * { margin: 0; padding: 0; box-sizing: border-box; }
  html, body {
    width: 818px; height: 1200px; overflow: hidden;
    background: var(--stage);
    font-family: "Alegreya Sans", sans-serif;
  }
  .sign {
    position: absolute; left: 115px; top: 28px;
    width: 891px; height: 1732px;
    transform: scale(0.66); transform-origin: top left;
    overflow: hidden;
    background: linear-gradient(150deg, var(--paper) 0%, var(--paper-shade) 45%, var(--paper) 100%);
  }
  .sign-shapes { position: absolute; inset: 0; width: 891px; height: 1732px; }
  .brand-mark {
    position: absolute; left: 370px; top: 170px; width: 150px; height: 150px;
    background: var(--brand-blue); opacity: 0.9;
  }
  .brand-name {
    position: absolute; left: 0; width: 891px; top: 380px;
    text-align: center; color: var(--brand-blue);
    font-weight: 800; font-size: 64px; letter-spacing: 4px; line-height: 1;
  }
  .heading-box {
    position: absolute; left: 92px; height: 106px;
    border: 2px solid var(--white); border-left-width: 2px;
    border-radius: 0 12px 12px 0;
    color: var(--white); font-weight: 900; font-size: 92px;
    line-height: 102px; padding-left: 54px; letter-spacing: 1px;
  }
  .heading-services { top: 669px; width: 522px; }
  .heading-hiring { top: 1044px; width: 695px; }
  .item-list { position: absolute; left: 118px; list-style: none; color: var(--white); }
  .item-list li { position: relative; padding-left: 40px; }
  .item-list li::before {
    content: "»"; position: absolute; left: 0; top: -2px; font-weight: 700;
  }
  .services-list { top: 800px; font-size: 40px; font-weight: 700; line-height: 55px; }
  .hiring-list { top: 1175px; font-size: 39px; font-weight: 900; line-height: 58px; text-transform: uppercase; }
  .contact { position: absolute; left: 143px; color: var(--white); font-weight: 800; display: flex; align-items: center; }
  .contact svg { flex: none; margin-right: 16px; }
  .contact-phone { top: 1455px; font-size: 84px; line-height: 84px; letter-spacing: 1px; }
  .contact-email { top: 1550px; font-size: 44px; line-height: 46px; }
  .contact-web { top: 1617px; font-size: 44px; line-height: 46px; }
  .licence {
    position: absolute; left: 800px; top: 1662px;
    transform: rotate(-90deg); transform-origin: top left;
    color: var(--white); font-weight: 700; font-size: 32px; letter-spacing: 1px;
    white-space: nowrap;
  }
</style>
</head>
<body>
<div class="sign">
  <svg class="sign-shapes" viewBox="0 0 891 1732" aria-hidden="true">
    <polygon points="0,482 891,700 891,1262 0,1479" fill="var(--brand-blue)"/>
    <polygon points="558,617 891,537 891,700" fill="var(--panel-grey)"/>
    <polygon points="0,1479 891,1262 891,1732 0,1732" fill="var(--ink-black)"/>
  </svg>

  <div class="brand-mark"></div>
  <div class="brand-name">MARLOW PAVING</div>

  <div class="heading-box heading-services">SERVICES</div>
  <ul class="item-list services-list">
    <li>Road Construction</li>
    <li>Site Preparation &amp; Excavation</li>
    <li>Underground Utilities</li>
    <li>Shoreline Restoration</li>
  </ul>

  <div class="heading-box heading-hiring">NOW HIRING</div>
  <ul class="item-list hiring-list">
    <li>Pipe Layers</li>
    <li>Equipment Operators</li>
    <li>Foremen</li>
  </ul>

  <div class="contact contact-phone">
    <svg width="60" height="60" viewBox="0 0 60 60" aria-hidden="true">
      <circle cx="30" cy="30" r="27" fill="none" stroke="#fff" stroke-width="3"/>
      <path d="M21 16c-3 2-5 5-3 11 3 8 9 14 17 17 5 2 8 0 10-3l-6-6-4 3c-4-2-7-5-9-9l3-4z" fill="none" stroke="#fff" stroke-width="3" stroke-linejoin="round"/>
    </svg>
    <span>555-382-9146</span>
  </div>
  <div class="contact contact-email">
    <svg width="60" height="40" viewBox="0 0 60 40" aria-hidden="true">
      <rect x="8" y="6" width="44" height="28" fill="none" stroke="#fff" stroke-width="2.5"/>
      <path d="M8 6l22 17 22-17M8 34l16-14M52 34L36 20" fill="none" stroke="#fff" stroke-width="2.5"/>
    </svg>
    <span>Info@MarlowPaving.example</span>
  </div>
  <div class="contact contact-web">
    <svg width="60" height="44" viewBox="0 0 60 44" aria-hidden="true">
      <circle cx="30" cy="22" r="19" fill="none" stroke="#fff" stroke-width="2.5"/>
      <ellipse cx="30" cy="22" rx="8" ry="19" fill="none" stroke="#fff" stroke-width="2.5"/>
      <path d="M11 22h38M14 12h32M14 32h32" stroke="#fff" stroke-width="2.5"/>
    </svg>
    <span>www.MarlowPaving.example</span>
  </div>
  <div class="licence">CUC 8047319</div>
</div>
</body>
</html>
```